Automotive eCommerce Business looking for a business card design

Looking for a clean and simple business card design. Our company name is "Harbor Crest Auto" and we are a company specializing in the ecommerce sales of automotive parts, specifically for pick up trucks and large SUVs. Our company colours are red, black, and white.

Feel free to use the logo provided or create a new logo that you seem fit. Looking forward to your creative ideas!

Industry/Entity Type

Automotive

Contact Information for Business Card

We were thinking of a possibly two-sided design featuring just the logo and company name on one side, and personal information on the other side. Single sided designs will be considered as well.

Font styles to use
Serif
Sans Serif
Decorative

Colors
ec1f27
ffffff
000000

Requirements
Must have
• Space for employee's name, title, phone number and email address, along with the company address and website somewhere.

```html
<!DOCTYPE html>
<html lang="en">
<head>
<meta charset="utf-8">
<title>Harbor Crest Auto – Business Card</title>
<link rel="stylesheet" href="https://fonts.googleapis.com/css2?family=Libre+Baskerville&family=Lato:wght@400;700&display=swap">
<style>
  :root {
    --brand-red: #a01920;
    --brand-red-light: #b51c24;
    --paper-white: #f2f2f0;
    --ink-black: #111111;
    --stage-grey: #b9b9b9;
    --white: #ffffff;
  }
  * { box-sizing: border-box; margin: 0; padding: 0; }
  html, body {
    width: 1200px;
    height: 1200px;
    overflow: hidden;
    background: var(--stage-grey);
  }
  .canvas {
    position: relative;
    width: 1200px;
    height: 1200px;
  }
  .card {
    position: absolute;
    left: 250px;
    width: 700px;
    height: 400px;
    overflow: hidden;
    box-shadow: 0 6px 18px rgba(0,0,0,0.18);
  }
  .card--front { top: 150px; background: var(--brand-red); }
  .card--back { top: 650px; display: flex; }

  /* Front */
  .front__pattern {
    position: absolute;
    left: 0; top: 150px;
    width: 100%; height: 180px;
    background: linear-gradient(180deg, rgba(120,10,16,0) 0%, rgba(120,10,16,0.35) 100%);
  }
  .front__brand {
    position: absolute;
    top: 90px; left: 0; width: 100%;
    display: flex; flex-direction: column; align-items: center; gap: 18px;
  }
  .brand-dot {
    width: 56px; height: 56px; border-radius: 50%;
    background: var(--white);
    flex: none;
  }
  .front__name {
    font-family: "Libre Baskerville", serif;
    font-size: 34px;
    color: var(--white);
    white-space: nowrap;
  }
  .front__band {
    position: absolute;
    left: 0; bottom: 0; width: 100%; height: 70px;
    background: var(--paper-white);
    display: flex; align-items: center; justify-content: center;
  }
  .front__tagline {
    font-family: "Lato", sans-serif;
    font-size: 21px;
    color: var(--brand-red);
    letter-spacing: 0.2px;
    white-space: nowrap;
  }

  /* Back */
  .back__brand-side {
    width: 50%;
    padding: 0 24px;
    background: var(--paper-white);
    display: flex; flex-direction: column; align-items: center; justify-content: center; gap: 22px;
    border-right: 4px solid var(--ink-black);
    text-align: center;
  }
  .brand-dot--red { background: var(--brand-red-light); width: 70px; height: 70px; }
  .back__name {
    font-family: "Libre Baskerville", serif;
    font-size: 22px;
    color: var(--ink-black);
    white-space: nowrap;
  }
  .back__info-side {
    flex: 1;
    background: var(--brand-red-light);
    color: var(--white);
    padding: 44px 36px 36px 24px;
    text-align: right;
    display: flex; flex-direction: column;
  }
  .person__name {
    font-family: "Libre Baskerville", serif;
    font-weight: 400;
    font-size: 28px;
    white-space: nowrap;
  }
  .person__title {
    font-family: "Lato", sans-serif;
    font-size: 15px;
    margin-top: 4px;
  }
  .person__rule {
    align-self: flex-end;
    width: 120px; height: 3px;
    background: var(--white);
    margin-top: 10px;
  }
  .contact {
    list-style: none;
    margin-top: auto;
    font-family: "Lato", sans-serif;
    font-size: 17px;
    line-height: 1.45;
  }
  .contact li { display: flex; justify-content: flex-end; align-items: center; gap: 8px; white-space: nowrap; }
  .contact svg { width: 14px; height: 14px; fill: var(--white); flex: none; }
  .contact .icon-space { width: 14px; flex: none; }
</style>
</head>
<body>
<main class="canvas">
  <section class="card card--front" aria-label="Business card front">
    <div class="front__pattern" role="img" aria-label="Fine connected-line network pattern across the red field"></div>
    <div class="front__brand">
      <span class="brand-dot"></span>
      <span class="front__name">Harbor Crest Auto Ltd.</span>
    </div>
    <div class="front__band">
      <p class="front__tagline">Specializing in The E-commerce Sales of Automotive Parts</p>
    </div>
  </section>

  <section class="card card--back" aria-label="Business card back">
    <div class="back__brand-side">
      <span class="brand-dot brand-dot--red"></span>
      <span class="back__name">Harbor Crest Auto Ltd.</span>
    </div>
    <div class="back__info-side">
      <h1 class="person__name">Marcus Delaney</h1>
      <p class="person__title">Managing Director</p>
      <span class="person__rule"></span>
      <ul class="contact">
        <li>555.014.2290
          <svg viewBox="0 0 24 24" aria-hidden="true"><path d="M6.6 10.8a15 15 0 0 0 6.6 6.6l2.2-2.2c.3-.3.7-.4 1-.2 1.1.4 2.3.6 3.6.6.6 0 1 .4 1 1V20c0 .6-.4 1-1 1C10.6 21 3 13.4 3 4c0-.6.4-1 1-1h3.5c.6 0 1 .4 1 1 0 1.3.2 2.5.6 3.6.1.3 0 .7-.2 1z"/></svg>
        </li>
        <li>info@harborcrestauto.com
          <svg viewBox="0 0 24 24" aria-hidden="true"><path d="M2 5h20v14H2z M4 7v.5l8 5 8-5V7l-8 5z" fill-rule="evenodd"/></svg>
        </li>
        <li>www.harborcrestauto.com
          <svg viewBox="0 0 24 24" aria-hidden="true"><path d="M12 2a10 10 0 1 0 0 20 10 10 0 0 0 0-20zm-1 2.1V8H7.5A8 8 0 0 1 11 4.1zM13 4.1A8 8 0 0 1 16.5 8H13zM4.3 10H11v4H4.3a8 8 0 0 1 0-4zM13 10h6.7a8 8 0 0 1 0 4H13zM7.5 16H11v3.9A8 8 0 0 1 7.5 16zM13 16h3.5a8 8 0 0 1-3.5 3.9z"/></svg>
        </li>
        <li>48 Linden Avenue,
          <svg viewBox="0 0 24 24" aria-hidden="true"><path d="M12 3 2 12h3v8h5v-5h4v5h5v-8h3z"/></svg>
        </li>
        <li>Portland, USA <span class="icon-space"></span></li>
      </ul>
    </div>
  </section>
</main>
</body>
</html>
```